Business Card Design Project

I need a business card design for my law office. I already have a logo.

I am an employment attorney who represents clients who have been wrongfully terminated or have been discriminated against by their employer.

I would like a unique, clean design using the colors in the logo or colors that complement the logo.

Target Market(s)

Clients, potential clients, other attorneys and others.

Industry/Entity Type

Attorney

Requirements
Must have
• I would like to use both sides of the card.

The information on the card must be easy to read.

Here is my information:

T. Dale Everhoff
3857 E. Pallister Rd., Suite 204
Valley Oaks, California 93790
559-731-4086
559-862-5143 fax
dale@lawtde.example
Nice to have
• QR Code? I would like to see designs incorporating a nice-looking QR code. Look at this example:

Notice the second QR code in the article - the color.

```html
<!DOCTYPE html>
<html lang="en">
<head>
<meta charset="utf-8">
<title>T. Dale Everhoff Law Office – Business Card</title>
<link rel="stylesheet" href="https://fonts.googleapis.com/css2?family=Ledger&display=swap">
<style>
  :root {
    --card-top: #e9ebcc;
    --card-bottom: #c0c390;
    --ink: #7880c0;
    --brand: #2b78c4;
    --brand-deep: #2c3f8f;
  }
  * { margin: 0; padding: 0; box-sizing: border-box; }
  html, body {
    width: 1200px;
    height: 720px;
    overflow: hidden;
  }
  body { background: var(--card-bottom); }
  .card {
    position: relative;
    width: 1200px;
    height: 720px;
    background: linear-gradient(180deg, var(--card-top) 0%, var(--card-bottom) 100%);
    font-family: "Ledger", Georgia, serif;
    font-weight: 400;
    color: var(--ink);
  }
  .brand-mark {
    position: absolute;
    left: 252px;
    top: 112px;
    width: 88px;
    height: 88px;
    background: var(--brand);
  }
  .brand-name {
    position: absolute;
    right: 293px;
    top: 104px;
    font-size: 58px;
    line-height: 1;
    color: var(--brand);
    white-space: nowrap;
    text-align: right;
  }
  .brand-office {
    position: absolute;
    right: 293px;
    top: 186px;
    font-size: 30px;
    line-height: 1;
    letter-spacing: 0.3em;
    margin-right: -0.3em;
    text-transform: uppercase;
    color: var(--brand);
    white-space: nowrap;
  }
  .address {
    position: absolute;
    right: 290px;
    top: 300px;
    text-align: right;
    font-style: normal;
    font-size: 34px;
    line-height: 57px;
    letter-spacing: 0.02em;
    white-space: nowrap;
  }
  .phone {
    position: absolute;
    left: 494px;
    width: 400px;
    top: 430px;
    text-align: center;
    font-size: 34px;
    letter-spacing: 0.02em;
  }
  .secondary-contact {
    position: absolute;
    left: 55px;
    top: 558px;
    font-size: 34px;
    line-height: 48px;
    letter-spacing: 0.02em;
    white-space: nowrap;
  }
</style>
</head>
<body>
  <main class="card">
    <span class="brand-mark" aria-hidden="true"></span>
    <div class="brand-name">T. Dale Everhoff</div>
    <div class="brand-office">Law Office</div>

    <address class="address">
      <div class="address-line">3857 E. Pallister Rd., Suite 204</div>
      <div class="address-line">Valley Oaks, California 93790</div>
    </address>

    <div class="phone">559-731-4086</div>

    <div class="secondary-contact">
      <div class="fax">Fax # : 559-862-5143</div>
      <div class="email">mail:dale@lawtde.example</div>
    </div>
  </main>
</body>
</html>
```